Dinner Invitation for an email

Please create an image I can embed in an email. The tone should be sophisticated, fun and festive.

Here is the copy:

FOOD | FRIENDS | FUN
Please join BRV and friends at Corvetti's Harbor House for cocktails, conversation and a delectable dinner
Date: Monday, January 23 (during OPMI)
Time: Cocktails start at 6:30 | Dinner is around 7
Place: Corvetti's Harbor House - The Pearl Terrace
27318 W Dunmore Pkwy - Scottsdale
(Adjacent to the Halvorsen Pinecrest Lodge)

RSVP: mara.quinby@brvholdco.example
(Mara will send you a calendar invite)

Hope to see you there!

```html
<!DOCTYPE html>
<html lang="en">
<head>
<meta charset="utf-8">
<title>BRV Dinner Invitation – Options</title>
<link rel="stylesheet" href="https://fonts.googleapis.com/css2?family=Cinzel:wght@400&family=Sorts+Mill+Goudy&family=Yellowtail&display=swap">
<style>
  :root {
    --page: #ffffff;
    --ink: #2b2b2b;
    --paper: #f4f4f2;
    --frame: #ffffff;
    --brand: #123a8c;
    --photo-dark: #3a302c;
    --photo-mid: #6b544a;
    --photo-warm: #9a6d58;
    --photo-light: #b9b3b0;
  }
  * { box-sizing: border-box; margin: 0; padding: 0; }
  html, body { width: 1200px; height: 927px; overflow: hidden; background: var(--page); }
  .board { position: relative; width: 1200px; height: 927px; }

  .option-title {
    position: absolute; top: 80px; width: 527px;
    text-align: center; font-family: "Cinzel", serif;
    font-size: 27px; letter-spacing: 4px; color: var(--ink);
  }
  .option-title.first { left: 51px; }
  .option-title.second { left: 614px; }

  .invite { position: absolute; top: 131px; width: 527px; height: 659px; }
  .invite.first { left: 51px; }
  .invite.second { left: 614px; }

  .backdrop {
    position: absolute; inset: 0;
    background:
      radial-gradient(ellipse 40% 20% at 25% 8%, var(--photo-light), transparent 70%),
      radial-gradient(ellipse 30% 40% at 8% 35%, var(--photo-warm), transparent 75%),
      radial-gradient(ellipse 35% 45% at 92% 55%, var(--photo-mid), transparent 75%),
      linear-gradient(160deg, var(--photo-mid) 0%, var(--photo-dark) 55%, #4a3a34 100%);
  }
  .frame-line {
    position: absolute; left: 77px; top: 97px; width: 375px; height: 469px;
    border: 1px solid var(--frame);
  }
  .panel {
    position: absolute; left: 83px; top: 105px; width: 362px; height: 453px;
    background: var(--paper);
  }

  .line {
    position: absolute; left: 0; right: 0; text-align: center;
    color: var(--ink); line-height: 1; white-space: nowrap;
  }
  .headline { font-family: "Cinzel", serif; font-size: 16.5px; letter-spacing: 2.2px; }
  .intro { font-family: "Sorts Mill Goudy", serif; font-size: 12.5px; }
  .label { font-family: "Sorts Mill Goudy", serif; font-size: 13px; text-transform: uppercase; }
  .detail { font-family: "Sorts Mill Goudy", serif; font-size: 8.6px; text-transform: uppercase; letter-spacing: 1.6px; }
  .detail.small { font-size: 7.4px; letter-spacing: 1.1px; }
  .closing { font-family: "Yellowtail", cursive; font-size: 15px; }
  .rule { position: absolute; left: 50%; width: 48px; margin-left: -24px; border-top: 1px solid var(--ink); }

  .brand-mark {
    position: absolute; left: 0; right: 0; display: flex; justify-content: center; align-items: center; gap: 6px;
    font-family: "Sorts Mill Goudy", serif; font-size: 15px; color: var(--brand); letter-spacing: 1px;
  }
  .brand-mark .square { width: 12px; height: 12px; background: var(--brand); }
</style>
</head>
<body>
<main class="board">
  <h2 class="option-title first">OPTION 1</h2>
  <h2 class="option-title second">OPTION 2</h2>

  <!-- Option 1: brand at the foot -->
  <section class="invite first">
    <div class="backdrop" role="img" aria-label="Blurred photo of guests raising champagne and cocktail glasses in a toast, warm bokeh lights"></div>
    <div class="frame-line"></div>
    <div class="panel"></div>
    <p class="line headline" style="top:144px">FOOD | FRIENDS | FUN</p>
    <p class="line intro" style="top:191px">Please join BRV and friends at Corvetti's Harbor House</p>
    <p class="line intro" style="top:206px">for cocktails, conversation and a delectable dinner.</p>
    <p class="line label" style="top:243px">Date</p>
    <p class="line detail" style="top:261px">Monday, January 23 (during OPMI)</p>
    <p class="line label" style="top:288px">Time</p>
    <p class="line detail" style="top:306px">Cocktails start at 6:30 | Dinner is around 7</p>
    <p class="line label" style="top:332px">Place</p>
    <p class="line detail" style="top:349px">Corvetti's Harbor House – The Pearl Terrace</p>
    <p class="line detail small" style="top:366px">27318 W Dunmore Pkwy – Scottsdale</p>
    <p class="line detail small" style="top:376px">(Adjacent to the Halvorsen Pinecrest Lodge)</p>
    <p class="line label" style="top:399px">RSVP</p>
    <p class="line detail" style="top:417px">mara.quinby@brvholdco.example</p>
    <p class="line detail small" style="top:428px">( Mara will send you a calendar invite )</p>
    <span class="rule" style="top:457px"></span>
    <p class="line closing" style="top:471px">Hope to see you there!</p>
    <div class="brand-mark" style="top:514px"><span class="square"></span>BRV</div>
  </section>

  <!-- Option 2: brand at the head -->
  <section class="invite second">
    <div class="backdrop" role="img" aria-label="Blurred photo of guests raising champagne and cocktail glasses in a toast, warm bokeh lights"></div>
    <div class="frame-line"></div>
    <div class="panel"></div>
    <div class="brand-mark" style="top:140px"><span class="square"></span>BRV</div>
    <p class="line headline" style="top:194px">FOOD | FRIENDS | FUN</p>
    <p class="line intro" style="top:236px">Please join BRV and friends at Corvetti's Harbor House</p>
    <p class="line intro" style="top:251px">for cocktails, conversation and a delectable dinner.</p>
    <p class="line label" style="top:285px">Date</p>
    <p class="line detail" style="top:303px">Monday, January 23 (during OPMI)</p>
    <p class="line label" style="top:329px">Time</p>
    <p class="line detail" style="top:347px">Cocktails start at 6:30 | Dinner is around 7</p>
    <p class="line label" style="top:373px">Place</p>
    <p class="line detail" style="top:391px">Corvetti's Harbor House – The Pearl Terrace</p>
    <p class="line detail small" style="top:407px">27318 W Dunmore Pkwy – Scottsdale</p>
    <p class="line detail small" style="top:416px">(Adjacent to the Halvorsen Pinecrest Lodge)</p>
    <p class="line label" style="top:440px">RSVP</p>
    <p class="line detail" style="top:457px">mara.quinby@brvholdco.example</p>
    <p class="line detail small" style="top:469px">( Mara will send you a calendar invite )</p>
    <span class="rule" style="top:498px"></span>
    <p class="line closing" style="top:516px">Hope to see you there!</p>
  </section>
</main>
</body>
</html>
```